Retail Pack Frozen Food Items

Hi - I would like to create a series of retail pack frozen food labels for various items. Please see the example label attacked and create an editable label file as I will be using this file for multiple products. Please include the same verbage for the safe handling with editable text. Label needs to have labels sections for the product name, establishment number , keep frozen, net weight section, Best by Date Section, Section for UPC code , and for the bottom right we can use "Packed for Korvel Foods Inc 4873 Pelham Ave Santa Clara, CA 95187" . i have also attached our logo for the upper left hand corner to use. please create one in black and white and one version using the blue logo. Again all fields will be editable as we will use this same file to create multiple labels of different products.

```html
<!DOCTYPE html>
<html lang="en">
<head>
<meta charset="utf-8">
<title>Korvel Foods – Frozen Retail Label</title>
<link rel="stylesheet" href="https://fonts.googleapis.com/css2?family=Roboto:wght@500;700;900&family=Barlow+Semi+Condensed:wght@400&family=Arimo:wght@400;700&family=Archivo:wght@800&display=swap">
<style>
  :root{
    --brand-blue:#1f6898;
    --panel-blue:#ddeffa;
    --upc-grey:#ececec;
    --stage:#c4c4c4;
    --ink:#000000;
    --paper:#ffffff;
  }
  *{box-sizing:border-box;margin:0;padding:0}
  html,body{width:1200px;height:828px;overflow:hidden;background:var(--stage)}
  .label{position:absolute;left:40px;top:58px;width:1120px;height:713px;background:var(--paper);color:var(--ink)}
  .header{position:absolute;left:35px;top:27px;width:1050px;height:238px;background:var(--brand-blue);border-radius:13px}
  .brand{position:absolute;left:30px;top:14px;width:212px;height:212px;border:8px solid var(--paper);border-radius:50%;display:flex;align-items:center;justify-content:center}
  .brand-name{font-family:"Roboto",sans-serif;font-weight:700;font-size:23px;color:var(--paper);letter-spacing:.3px;white-space:nowrap}
  .product-name{position:absolute;left:258px;top:50px;width:520px;text-align:center;font-family:"Roboto",sans-serif;font-weight:700;font-size:66px;line-height:70px;color:var(--paper);white-space:nowrap}
  .est-box{position:absolute;left:798px;top:51px;width:222px;height:137px;background:var(--paper);font-family:"Arimo",sans-serif;font-size:18px;line-height:28px;text-align:center;padding-top:28px}
  .keep-frozen{position:absolute;left:48px;top:281px;font-family:"Roboto",sans-serif;font-weight:700;font-size:46px;line-height:46px;letter-spacing:.3px}
  .handling{position:absolute;left:35px;top:328px;width:597px;height:332px;background:var(--panel-blue)}
  .handling h2{position:absolute;left:13px;top:18px;font-family:"Roboto",sans-serif;font-weight:700;font-size:24px;line-height:26px}
  .handling .intro{position:absolute;left:13px;top:54px;width:580px;font-family:"Barlow Semi Condensed",sans-serif;font-size:22px;line-height:26px;white-space:nowrap}
  .step{position:absolute;font-family:"Barlow Semi Condensed",sans-serif;font-size:21.5px;line-height:25.5px;white-space:nowrap}
  .step svg{position:absolute;left:-52px;top:2px;width:42px;height:62px;fill:none;stroke:var(--ink);stroke-width:1.6;stroke-linecap:round;stroke-linejoin:round}
  .step-1{left:73px;top:127px}
  .step-2{left:357px;top:127px}
  .step-3{left:73px;top:235px}
  .step-4{left:357px;top:235px}
  .net-wt,.best-by{position:absolute;left:683px;font-family:"Arimo",sans-serif;font-weight:700;font-size:30px;line-height:32px;white-space:nowrap}
  .net-wt{top:294px}
  .best-by{top:346px}
  .upc-area{position:absolute;left:683px;top:401px;width:385px;height:139px;background:var(--upc-grey)}
  .packer{position:absolute;left:683px;top:555px;font-family:"Arimo",sans-serif;font-size:22px;line-height:26.5px;font-style:normal}
  .packer strong{display:block;font-family:"Archivo",sans-serif;font-weight:800;font-size:25px;line-height:30px;margin-bottom:2px;white-space:nowrap}
  .footer-band{position:absolute;left:0;bottom:0;width:1120px;height:34px;background:var(--brand-blue)}
</style>
</head>
<body>
<main class="label">
  <header class="header">
    <div class="brand"><span class="brand-name">KORVEL FOODS</span></div>
    <h1 class="product-name">Pork Grade A<br>Sparerib Cut</h1>
    <div class="est-box">Establishment No:<br>EST. ###</div>
  </header>

  <p class="keep-frozen">KEEP FROZEN</p>

  <section class="handling">
    <h2>SAFE HANDLING INSTRUCTIONS</h2>
    <p class="intro">Some food products may contain bacteria that could cause<br>illness if mishandled. Follow these instructions for your safety:</p>

    <div class="step step-1">
      <svg viewBox="0 0 42 62"><rect x="3" y="2" width="35" height="58" rx="4"/><line x1="3" y1="15" x2="38" y2="15"/><line x1="3" y1="52" x2="38" y2="52"/><line x1="32" y1="32" x2="32" y2="46"/></svg>
      <p>Keep refrigerated or<br>frozen. Thaw in<br>refrigerator.</p>
    </div>
    <div class="step step-2">
      <svg viewBox="0 0 52 62" style="width:52px;left:-64px"><path d="M2 8h12q6 0 6 6v4"/><path d="M17 22v8M21 22v12M25 24v10"/><path d="M4 40h18l6 4h20M6 46h14M6 52h16l6 4h20"/><path d="M30 24l18-8M30 30l18-4"/></svg>
      <p>Wash working surfaces,<br>utensils, and hands after<br>touching raw product.</p>
    </div>
    <div class="step step-3">
      <svg viewBox="0 0 42 76" style="height:76px"><ellipse cx="18" cy="10" rx="15" ry="8"/><ellipse cx="18" cy="10" rx="6" ry="3"/><path d="M4 30h30M28 25l6 5-6 5M14 25l-8 5 8 5"/><path d="M22 46c6-4 14 2 10 9l-10 12c-4 4-10-2-6-6z"/></svg>
      <p>Keep raw meat and<br>poultry separate from<br>other foods.</p>
    </div>
    <div class="step step-4">
      <svg viewBox="0 0 52 62" style="width:52px;left:-64px"><path d="M18 2c-3 3 3 5 0 9M26 2c-3 3 3 5 0 9M34 2c-3 3 3 5 0 9"/><path d="M6 20h40M4 24h4M44 24h4"/><path d="M10 20v16q0 4 4 4h24q4 0 4-4V20"/><path d="M14 52l4-6 4 6zM24 52l4-6 4 6zM34 52l4-6 4 6zM10 54h34"/></svg>
      <p>Cook thoroughly. Keep<br>hot foods hot. Refrigerate<br>leftovers immediately.</p>
    </div>
  </section>

  <p class="net-wt">Net Wt: 16 oz (1 lb) 454 g</p>
  <p class="best-by">Best By: MM/DD/YYYY</p>
  <div class="upc-area" role="img" aria-label="Space reserved for UPC code"></div>

  <address class="packer">
    <strong>Packed for Korvel Foods Inc</strong>
    4873 Pelham Ave,<br>Santa Clara,<br>CA 95187
  </address>

  <div class="footer-band"></div>
</main>
</body>
</html>
```